Business Card/ Email Signature Design Project

I am an Interior Designer. I need a business card that looks sophisticated stylish but simple in design. My work covers space design/ interior architecture/ furniture design/ product development & styling.

I have a very specific brief and know mostly what I want. I'm hoping to work with someone who can translate my ideas.

My branding should have a strong focus on my name, the majority of my work is referral based.
I'm keen to keep a monochromatic colour scheme: dark charcoal/ black/ white/ embossing/ silver. I'm not suggesting we use all that I've listed, they are possible ideas at this stage. I will need to be mindful of printing costs an also how I make the design work across, cards, letter heads, email logo and web design.

Theory behind images sent below;
1-Rug Image_(minus boarder) I was thinking this image could be used on the back of the card with my contact details over. I like that the lines are almost hand drawn and start to look free form. It's a subtle contrast to a more formal front of the card with my name.
2_Owen Ratley_I really like the orientation, the proportion of font on the card, the colour and the font. I like the lower case for my name and the upper case for 'Interior Design'. Not sure if it should be 'Interior Designer or Interior Design' at this stage, was leaning towards 'Interior Design'. Was thinking the 'i' and 'd' in my surname could be the colour eg 'silver'?? We can decide on this once we see it.

Look forward to hearing from you.
Cheers,
Noreen Bastoli

Industry/Entity Type

Printing

Logo Text

Noreen Bastoli Interior Design

```html
<!DOCTYPE html>
<html lang="en">
<head>
<meta charset="utf-8">
<title>Noreen Bastoli Interior Design – Business Card</title>
<link rel="stylesheet" href="https://fonts.googleapis.com/css2?family=Arimo:wght@400;700&display=swap">
<style>
  :root {
    --backdrop: #e9e6e1;
    --rug-light: #dcd8d1;
    --rug-mid: #cbc6be;
    --ink: #1c1c1c;
    --shadow: rgba(0, 0, 0, 0.28);
  }
  html, body {
    margin: 0;
    padding: 0;
    overflow: hidden;
  }
  .canvas {
    position: relative;
    width: 1200px;
    height: 1000px;
    background: var(--backdrop);
    overflow: hidden;
    font-family: "Arimo", Arial, sans-serif;
  }
  .card {
    position: absolute;
    width: 729px;
    height: 417px;
    overflow: hidden;
    box-shadow: 0 4px 14px var(--shadow);
  }
  .card-front { left: 28px; top: 140px; }
  .card-back { left: 427px; top: 425px; }
  .rug-texture {
    position: absolute;
    inset: 0;
    background: linear-gradient(135deg, var(--rug-light) 0%, var(--rug-mid) 55%, var(--rug-light) 100%);
  }
  .brand {
    position: absolute;
    margin: 0;
    color: var(--ink);
    font-weight: 700;
    line-height: 1.12;
    letter-spacing: 0;
  }
  .brand-line { display: block; }

  .card-front .brand { left: 148px; top: 168px; font-size: 42px; }

  .card-back .brand { right: 26px; top: 50px; text-align: right; font-size: 24px; }

  .contact-list {
    position: absolute;
    left: 26px;
    top: 264px;
    margin: 0;
    padding: 0;
    list-style: none;
    color: var(--ink);
    font-weight: 700;
    font-size: 14.5px;
    letter-spacing: 3.2px;
    line-height: 25.5px;
  }
</style>
</head>
<body>
  <main class="canvas">
    <section class="card card-front">
      <div class="rug-texture" role="img" aria-label="Pale grey rug with hand-drawn charcoal hexagonal line pattern"></div>
      <h1 class="brand">
        <span class="brand-line">Noreen Bastoli</span>
        <span class="brand-line">Interior Design</span>
      </h1>
    </section>

    <section class="card card-back">
      <div class="rug-texture" role="img" aria-label="Pale grey rug with hand-drawn charcoal hexagonal line pattern"></div>
      <p class="brand">
        <span class="brand-line">Noreen Bastoli</span>
        <span class="brand-line">Interior Design</span>
      </p>
      <ul class="contact-list">
        <li class="contact-phone">0400 517 264</li>
        <li class="contact-web">www.noreenbastoli.com</li>
        <li class="contact-email">interiors@noreenbastoli.com</li>
        <li class="contact-address">P.O Box 207 Ashvale VIC. 3099</li>
      </ul>
    </section>
  </main>
</body>
</html>
```